meadowlight balance care (MBC)

I need to build a website for my therapy business.
There are two parts to the website
on the landing page; they choose whether they are therapists making a referral or patients needing more information.
After that, they are taken to their respective pages.
There is the textual information and a referral form on the therapist page, and on the patient page, the text is a bit different, and there will be a booking page on the patient page.
Visually minimal, it's a therapeutic website. I want it clean, clinical, and modern
colors: greenish blue or maybe orangish
PHP/html code
Updates

Hi everyone
I'm very sorry for the lack of responses to your designs. I am trying to work it out, but this platform has been a challenge for me.
I appreciate everyone's efforts, and I am unsure how to rate designs and move forward with the ones I like. There is a 5-star rating, but I don't understand how I'm supposed to politely say that it is not it without feeling like I'm going to affect someone's future rating negatively.
Please understand me. Thank you

Designs look the same

Target Market(s)

therapy and stress management

Industry/Entity Type

stress management therapy

Coding

Coded - Design and coding required

Number of Pages Required

5+ page

Font styles to use
Serif

Colors
0094D4
00A9DD
6FCCEA
C7EBF8
E9F6FB
00AB8E
00BBA5
67D7C9
C6EFE9
E9F9F6

Requirements
Must have
• landing page that that have 2 options. one for therapist another for patient

```html
<!DOCTYPE html>
<html lang="en">
<head>
<meta charset="utf-8">
<title>Meadowlight Balance Care</title>
<link href="https://fonts.googleapis.com/css2?family=Poppins:ital,wght@0,400;0,500;0,600;0,700;1,400&display=swap" rel="stylesheet">
<style>
:root{
  --board:#e8dac6;
  --blue:#0094d4;
  --blue-2:#00a9dd;
  --teal:#00ab8e;
  --teal-2:#00bba5;
  --teal-light:#67d7c9;
  --teal-pale:#c6efe9;
  --ink:#222;
  --text:#555;
  --grey-bg:#f4f4f4;
  --footer:#2e2e2e;
  --white:#fff;
}
*{box-sizing:border-box;margin:0;padding:0}
html,body{width:781px;height:1200px;overflow:hidden}
body{background:var(--board);font-family:'Poppins',sans-serif;position:relative;color:var(--text)}
.abs{position:absolute}

/* landing */
.landing{position:absolute;left:22px;top:24px;width:364px;height:224px;overflow:hidden}
.landing-photo{position:absolute;inset:0;background:linear-gradient(100deg,#0d4d8c 0%,#0b6f98 45%,#0a9a86 80%,#12a66a 100%)}
.landing-brackets{position:absolute;inset:0}
.landing-logo{position:absolute;left:132px;top:67px;width:101px;height:42px;border:1px solid rgba(255,255,255,.85);border-radius:3px;color:var(--white);text-align:center}
.landing-logo .mark{display:flex;align-items:center;justify-content:center;gap:6px;margin-top:5px}
.dot{width:14px;height:14px;border-radius:50%;background:var(--teal-light)}
.landing-logo .name{font-size:19px;font-weight:500;letter-spacing:5px;line-height:20px}
.landing-logo .tag{font-size:3.6px;font-weight:500;letter-spacing:.4px;margin-top:3px}
.choice{position:absolute;top:130px;width:73px;height:18px;border-radius:9px;font-size:5.5px;font-weight:600;color:var(--white);display:flex;align-items:center;justify-content:center;letter-spacing:.2px}
.choice-therapist{left:79px;background:var(--teal-2)}
.choice-patient{left:213px;border:1px solid var(--white)}
.landing-rule{position:absolute;left:0;right:0;top:198px;height:1px;background:rgba(255,255,255,.35)}
.copyright{font-size:4.2px;color:var(--white)}
.landing .copyright{position:absolute;left:23px;top:208px}
.socials{position:absolute;display:flex;gap:7px}
.socials span{width:7px;height:7px;border-radius:1.5px;background:var(--white)}
.landing .socials{left:278px;top:207px}

/* site */
.site{position:absolute;left:398px;top:24px;width:364px;height:1153px;overflow:hidden;background:var(--white)}
.hero{position:absolute;left:0;top:0;width:364px;height:187px;background:linear-gradient(100deg,#c9c5bd 0%,#ddd8cf 45%,#e9e4dc 70%,#d8d2c8 100%)}
.nav-logo{position:absolute;left:22px;top:11px;color:var(--white)}
.nav-logo .mark{display:flex;align-items:center;gap:4px}
.nav-logo .dot{width:11px;height:11px}
.nav-logo .name{font-size:14px;font-weight:500;letter-spacing:4px;line-height:15px}
.nav-logo .tag{font-size:2.6px;font-weight:600;letter-spacing:.2px;margin-top:2px}
.nav{position:absolute;left:90px;top:17px;display:flex;align-items:center;gap:0}
.nav a{font-size:5.2px;color:var(--white);text-decoration:none;margin-right:12px;line-height:10px}
.nav a.active{background:var(--blue);border-radius:5px;padding:0 7px}
.call{position:absolute;left:264px;top:12px;color:var(--white)}
.call .label{font-size:5px;font-weight:600}
.call .phone{font-size:9.2px;font-weight:600;letter-spacing:.3px;line-height:12px}
.referral{position:absolute;left:22px;top:69px;width:100px;height:100px;background:var(--white);border-radius:10px;padding:9px 8px}
.referral h2{font-size:7.5px;font-weight:600;color:var(--ink);margin-bottom:5px;letter-spacing:.1px}
.field{height:14px;border:1px solid #bbb;border-radius:7px;font-size:3.8px;color:#333;padding-left:6px;display:flex;align-items:center;margin-bottom:3px}
.submit{height:14px;background:var(--teal);border-radius:7px;color:var(--white);font-size:5px;font-weight:600;display:flex;align-items:center;justify-content:center;margin-top:1px}

.section-title{position:absolute;left:0;width:364px;text-align:center;font-size:12px;font-weight:600;line-height:16px}
.about-photo-main{position:absolute;left:22px;top:210px;width:156px;height:134px;background:linear-gradient(135deg,#9aa3ab,#c9cdd2 60%,#e4e2de)}
.about-photo-side{position:absolute;left:124px;top:279px;width:78px;height:75px;background:linear-gradient(135deg,#8b8178,#b9b5ad 60%,#d8d7d2);border:2px solid var(--white)}
.about-title{position:absolute;left:214px;top:226px;font-size:12.4px;font-weight:600;color:var(--blue)}
.about-text{position:absolute;left:214px;top:249px;width:130px;font-size:4.4px;line-height:9.2px;color:#333}
.btn-green{position:absolute;left:214px;top:322px;width:55px;height:16px;border-radius:8px;background:var(--teal);color:var(--white);font-size:5.6px;font-weight:600;display:flex;align-items:center;justify-content:center}

.services{position:absolute;left:0;top:381px;width:364px;height:194px;background:linear-gradient(100deg,#0a5f98 0%,#0a86b8 40%,#0aa092 75%,#087c74 100%)}
.services .section-title{top:22px;color:var(--white)}
.service-card{position:absolute;top:50px;width:73px;height:118px;border-radius:37px;background:var(--white);text-align:center;padding-top:12px}
.service-icon{width:34px;height:33px;margin:0 auto;border-radius:8px;background:var(--teal-pale)}
.service-card h3{font-size:7.4px;font-weight:600;color:var(--blue);margin-top:5px;line-height:10px}
.service-card p{font-size:4.5px;line-height:7.8px;color:#444;margin:3px 5px 0}

.team .section-title{top:609px;color:var(--blue)}
.member{position:absolute;top:621px;width:80px;text-align:center}
.avatar{width:64px;height:64px;border-radius:50%;margin:0 auto;background:radial-gradient(circle at 50% 40%,#d9d6d2,#a9a6a3)}
.member h3{font-size:6.6px;font-weight:600;color:var(--teal);margin-top:7px;line-height:10px}
.member p{font-size:4.5px;line-height:8.3px;color:#555;margin-top:1px}

.testimonials{position:absolute;left:0;top:756px;width:364px;height:146px;background:var(--grey-bg)}
.testimonials .section-title{top:15px;color:var(--blue)}
.quote-avatar{position:absolute;left:168px;top:40px;width:29px;height:29px;border-radius:50%;background:radial-gradient(circle,#d8d4cf,#a8a29b)}
.quote{position:absolute;left:32px;top:76px;width:300px;text-align:center;font-size:5.6px;font-style:italic;line-height:10.6px;color:#333}
.quote-name{position:absolute;left:0;width:364px;top:111px;text-align:center;font-size:5.4px;font-weight:600;color:var(--teal)}
.arrow{position:absolute;top:91px}

.news .section-title{top:920px;color:var(--ink)}
.news-card{position:absolute;top:946px;width:156px;height:160px;text-align:center}
.news-photo{width:156px;height:92px;border-radius:8px;background:linear-gradient(135deg,#b8b2a8,#e0ddd6 60%,#cfc8bc)}
.news-tab{position:absolute;left:12px;top:76px;width:132px;height:20px;background:var(--white);border-radius:10px 10px 0 0}
.news-date{position:absolute;left:0;width:156px;top:83px;font-size:6.6px;font-weight:500;color:var(--blue)}
.news-card h3{position:absolute;left:12px;width:132px;top:94px;font-size:7.4px;font-weight:400;color:var(--teal);line-height:9.8px}
.news-card p{position:absolute;left:14px;width:128px;top:117px;font-size:4.5px;line-height:7.8px;color:#444}

.site-footer{position:absolute;left:0;top:1112px;width:364px;height:41px;background:var(--footer)}
.site-footer .copyright{position:absolute;left:22px;top:18px}
.site-footer .socials{left:278px;top:17px}
</style>
</head>
<body>

<section class="landing">
  <div class="landing-photo" role="img" aria-label="City skyline by a river at dusk, tinted blue to green"></div>
  <svg class="landing-brackets" width="364" height="224" viewBox="0 0 364 224" aria-hidden="true">
    <path d="M132 78 H116 V130 M233 78 H250 V130" fill="none" stroke="#fff" stroke-width=".8"/>
  </svg>
  <div class="landing-logo">
    <div class="mark"><span class="dot"></span><span class="name">MBC</span></div>
    <div class="tag">MEADOWLIGHT BALANCE CARE</div>
  </div>
  <div class="choice choice-therapist">THERAPIST</div>
  <div class="choice choice-patient">PATIENT</div>
  <div class="landing-rule"></div>
  <p class="copyright">Copyright © 2022 Company Name.&nbsp; All Rights Reserved.</p>
  <div class="socials"><span></span><span></span><span></span><span></span><span></span></div>
</section>

<main class="site">
  <header class="hero" role="img" aria-label="Smiling therapist in glasses seated in a bright office">
  </header>
  <div class="nav-logo">
    <div class="mark"><span class="dot"></span><span class="name">MBC</span></div>
    <div class="tag">MEADOWLIGHT BALANCE CARE</div>
  </div>
  <nav class="nav">
    <a class="active">Home</a><a>About Us</a><a>Services</a><a>Blog</a><a>Contact Us</a>
  </nav>
  <div class="call">
    <div class="label">Call For Appointment</div>
    <div class="phone">1-800-555-0142</div>
  </div>
  <form class="referral">
    <h2>REFERRAL FORM</h2>
    <div class="field">Name</div>
    <div class="field">Email Address</div>
    <div class="field">Enter Referral Code</div>
    <div class="submit">Submit</div>
  </form>

  <section class="about">
    <div class="about-photo-main" role="img" aria-label="Therapist smiling at her desk"></div>
    <div class="about-photo-side" role="img" aria-label="Counselling session in a lounge"></div>
    <h2 class="about-title">About Therapist</h2>
    <p class="about-text">Sed ut perspiciatis unde omnis iste natus error sit voluptatem accusantium doloremque laudantium, totam rem aperiam, eaque ipsa quae ab illo inventore veritatis et quasi architecto beatae vitae dicta sunt explicabo. Nemo enim ipsam voluptatem quia voluptas sit aspernatur aut odit aut fugit, sed quia consequuntur magni dolores eos.</p>
    <div class="btn-green">Read More</div>
  </section>

  <section class="services" role="group" aria-label="Our Services">
    <div class="abs" style="inset:0" role="img" aria-label="Group therapy session, tinted blue and teal"></div>
    <h2 class="section-title">Our Services</h2>
    <div class="service-card" style="left:22px"><div class="service-icon" role="img" aria-label="Doctor with medical speech bubble"></div><h3>Service 1</h3><p>Sed ut perspiciatis unde omnis iste natus error sit voluptatem accusa ntium dolorem qui ratione voluptatem.</p></div>
    <div class="service-card" style="left:105px"><div class="service-icon" role="img" aria-label="Carer with a child"></div><h3>Service 2</h3><p>Sed ut perspiciatis unde omnis iste natus error sit voluptatem accusa ntium dolorem qui ratione voluptatem.</p></div>
    <div class="service-card" style="left:187px"><div class="service-icon" role="img" aria-label="Two people in conversation"></div><h3>Service 3</h3><p>Sed ut perspiciatis unde omnis iste natus error sit voluptatem accusa ntium dolorem qui ratione voluptatem.</p></div>
    <div class="service-card" style="left:268px"><div class="service-icon" role="img" aria-label="Physical therapy with wheelchair"></div><h3>Service 4</h3><p>Sed ut perspiciatis unde omnis iste natus error sit voluptatem accusa ntium dolorem qui ratione voluptatem.</p></div>
  </section>

  <section class="team">
    <h2 class="section-title">Our Team</h2>
    <div class="member" style="left:19px"><div class="avatar" role="img" aria-label="Team member portrait"></div><h3>Name Heading</h3><p>Sed ut perspiciatis unde omnis iste natus error sit voluptatem accusantium dolorem</p></div>
    <div class="member" style="left:101px"><div class="avatar" role="img" aria-label="Team member portrait"></div><h3>Name Heading</h3><p>Sed ut perspiciatis unde omnis iste natus error sit voluptatem accusantium dolorem</p></div>
    <div class="member" style="left:184px"><div class="avatar" role="img" aria-label="Team member portrait"></div><h3>Name Heading</h3><p>Sed ut perspiciatis unde omnis iste natus error sit voluptatem accusantium dolorem</p></div>
    <div class="member" style="left:266px"><div class="avatar" role="img" aria-label="Team member portrait"></div><h3>Name Heading</h3><p>Sed ut perspiciatis unde omnis iste natus error sit voluptatem accusantium dolorem</p></div>
  </section>

  <section class="testimonials">
    <h2 class="section-title">Testimonials</h2>
    <div class="quote-avatar" role="img" aria-label="Client portrait"></div>
    <svg class="arrow" style="left:17px" width="6" height="10" viewBox="0 0 6 10" aria-hidden="true"><path d="M5 1 1 5l4 4" fill="none" stroke="#333" stroke-width="1"/></svg>
    <p class="quote">Sed ut perspiciatis unde omnis iste natus error sit voluptatem accusantium doloremque error sit voluptatem accusantium doloremque laudantium, totam rem aperiam, eaque ipsa quae ab illo inventore veritatis et quasi architecto beatae vitae dicta sunt explicabo.</p>
    <svg class="arrow" style="left:341px" width="6" height="10" viewBox="0 0 6 10" aria-hidden="true"><path d="M1 1l4 4-4 4" fill="none" stroke="#333" stroke-width="1"/></svg>
    <div class="quote-name">Name Heading</div>
  </section>

  <section class="news">
    <h2 class="section-title">Latest News</h2>
    <article class="news-card" style="left:22px">
      <div class="news-photo" role="img" aria-label="Woman with headphones on a video call"></div>
      <div class="news-tab"></div>
      <div class="news-date">Aug02, 2022</div>
      <h3>Neque porro quisquam est, qui dolorem ipsum quia</h3>
      <p>Sed ut perspiciatis unde omnis iste natus error sit voluptatem accusa ntium dolorem qui ratione voluptatem magni dolores eos qui.</p>
    </article>
    <article class="news-card" style="left:186px">
      <div class="news-photo" role="img" aria-label="Two women talking in a counselling session"></div>
      <div class="news-tab"></div>
      <div class="news-date">Aug02, 2022</div>
      <h3>Neque porro quisquam est, qui dolorem ipsum quia</h3>
      <p>Sed ut perspiciatis unde omnis iste natus error sit voluptatem accusa ntium dolorem qui ratione voluptatem magni dolores eos qui.</p>
    </article>
  </section>

  <footer class="site-footer">
    <p class="copyright">Copyright © 2022 Company Name.&nbsp; All Rights Reserved.</p>
    <div class="socials"><span></span><span></span><span></span><span></span><span></span></div>
  </footer>
</main>

</body>
</html>
```